MOREVI VEGAN SUSHI

www.morevi-restaurant.de
We are open in 2018 and are an innovative restaurant from Munich. We would like a cool design for our drinks and food menu. It's very simple at the moment. See the File menu. In any case, our logo should appear. On the website we use neutraface as a font. But it's not a must. We are only open in the evening and appeal to a young, upscale audience.

```html
<!DOCTYPE html>
<html lang="de">
<head>
<meta charset="utf-8">
<title>MOREVI Vegan Sushi – Speisekarte</title>
<link rel="stylesheet" href="https://fonts.googleapis.com/css2?family=Abel&family=Yellowtail&display=swap">
<style>
  :root {
    --stage: #2a2630;
    --paper: #ebe3df;
    --paper-edge: #ded4cf;
    --ink: #1d1a1a;
    --accent: #c2491f;
    --rule: #8b817c;
    --salmon: #ee7a3a;
    --rice: #f3efe8;
    --sprout: #86b24a;
    --nori: #3b3f3a;
  }
  * { box-sizing: border-box; margin: 0; padding: 0; }
  html, body { width: 800px; height: 1200px; overflow: hidden; }
  body {
    background: var(--stage);
    font-family: "Abel", "Arial Narrow", sans-serif;
    color: var(--ink);
    position: relative;
  }
  .menu-pair {
    position: absolute;
    top: 325px;
    left: 8px;
    display: flex;
    gap: 8px;
  }
  .page {
    position: relative;
    width: 388px;
    height: 549px;
    background: radial-gradient(ellipse at 50% 45%, var(--paper) 60%, var(--paper-edge) 100%);
    overflow: hidden;
    box-shadow: 0 4px 14px rgba(0,0,0,.45);
  }
  .food-photo { position: absolute; }
  .food-photo.salmon {
    background: radial-gradient(ellipse at 50% 50%, var(--salmon) 0%, #f4a070 35%, var(--rice) 62%, rgba(243,239,232,0) 75%);
  }
  .food-photo.roll {
    background: radial-gradient(ellipse at 55% 50%, var(--rice) 0%, #d9c98e 40%, var(--nori) 60%, rgba(59,63,58,0) 74%);
  }
  .food-photo.sprout {
    background: radial-gradient(ellipse at 50% 50%, rgba(134,178,74,.55) 0%, rgba(134,178,74,.2) 40%, rgba(134,178,74,0) 70%);
  }
  .food-photo.fish {
    background: radial-gradient(ellipse at 40% 50%, #f6ece4 0%, #f0c6b0 45%, rgba(240,198,176,0) 72%);
  }

  .brand {
    position: absolute;
    top: 44px;
    left: 0;
    width: 100%;
    text-align: center;
    font-size: 24px;
    letter-spacing: 9px;
    text-indent: 9px;
    color: var(--ink);
  }
  .brand-rule {
    position: absolute;
    top: 112px;
    left: 14px;
    width: 350px;
    border-top: 1px dotted var(--rule);
  }

  .block {
    position: absolute;
    text-align: center;
    transform: translateX(-50%);
  }
  .block h2 {
    font-weight: 400;
    font-size: 11px;
    color: var(--accent);
    line-height: 1;
    padding: 4px 0 4px;
    border-top: 1px dotted var(--rule);
    border-bottom: 1px dotted var(--rule);
    margin-bottom: 4px;
    white-space: nowrap;
  }
  .block h2.open-top { border-top: none; }
  .block ul { list-style: none; }
  .block li {
    font-size: 7px;
    line-height: 11.4px;
    text-transform: none;
    white-space: nowrap;
  }
  .block li.wrap { white-space: normal; line-height: 9px; margin-bottom: 2px; }
  .block .price { color: var(--accent); font-size: 8px; }
  .block .note { font-size: 7px; line-height: 11px; margin-bottom: 11px; }
  .block.courses ul { line-height: 9px; }

  .chef   { top: 115px; left: 108px; width: 148px; }
  .omakase{ top: 115px; left: 284px; width: 166px; }
  .set-1  { top: 207px; left: 195px; width: 120px; }
  .set-2  { top: 329px; left: 195px; width: 120px; }
  .set-3  { top: 428px; left: 195px; width: 120px; }

  .starters { top: 117px; left: 198px; width: 134px; }
  .sushi    { top: 198px; left: 110px; width: 108px; }
  .small    { top: 198px; left: 278px; width: 108px; }
  .mains    { top: 317px; left: 110px; width: 130px; }
  .desserts { top: 317px; left: 278px; width: 108px; }

  .vegan-tag {
    position: absolute;
    top: 446px;
    left: 0;
    width: 100%;
    text-align: center;
    font-family: "Yellowtail", cursive;
    font-size: 16px;
    color: var(--accent);
  }
  .allergy-note {
    position: absolute;
    top: 476px;
    left: 0;
    width: 100%;
    text-align: center;
    font-size: 6.3px;
    line-height: 8.5px;
  }
</style>
</head>
<body>
<main class="menu-pair">

  <section class="page page-sets" aria-label="Menüs und Sets">
    <div class="food-photo salmon" style="left:-20px;top:-25px;width:130px;height:100px" role="img" aria-label="Foto: Sushi-Rolle mit Lachs"></div>
    <div class="food-photo roll" style="left:330px;top:-10px;width:80px;height:100px" role="img" aria-label="Foto: Sushi-Rolle mit Sesam"></div>
    <div class="food-photo sprout" style="left:-20px;top:120px;width:90px;height:90px" role="img" aria-label="Foto: Kressesprossen"></div>
    <div class="food-photo salmon" style="left:-25px;top:175px;width:85px;height:130px" role="img" aria-label="Foto: Sushi mit Lachs und Kaviar"></div>
    <div class="food-photo fish" style="left:-20px;top:300px;width:110px;height:80px" role="img" aria-label="Foto: Nigiri-Scheibe"></div>
    <div class="food-photo salmon" style="left:345px;top:230px;width:70px;height:140px" role="img" aria-label="Foto: Sushi-Rolle mit Lachs"></div>
    <div class="food-photo roll" style="left:-30px;top:445px;width:100px;height:120px" role="img" aria-label="Foto: Sushi-Rolle mit Stäbchen"></div>
    <div class="food-photo salmon" style="left:270px;top:465px;width:140px;height:100px" role="img" aria-label="Foto: Sushi mit Lachs und Sprossen"></div>

    <h1 class="brand">MOREVI</h1>
    <div class="brand-rule"></div>

    <div class="block chef courses">
      <h2 class="open-top">CHEF MENÜ mit Aperitiv &nbsp;81,00€</h2>
      <p class="note">für 2 Personen</p>
      <ul>
        <li class="wrap">Kleine Portion RAMENSUPPE mit Gemüse &amp; Nudeln</li>
        <li>MINI SET</li>
        <li>DESSERT</li>
      </ul>
    </div>
    <div class="block omakase courses">
      <h2 class="open-top">OMAKASE &nbsp;68,00€</h2>
      <p class="note">für 2 Personen</p>
      <ul>
        <li>EDAMAME</li>
        <li>OMAKASE SET mit 8 Spezialitäten des Hauses</li>
        <li>PANA COTTA mit Beeren</li>
      </ul>
    </div>

    <div class="block set-1">
      <h2>SET 1 &nbsp;&nbsp;33,90€</h2>
      <ul>
        <li>HOSOMAKI</li><li>FUTOMAKI</li><li>NIGIRI</li><li>KÜRBISKROKETTEN</li>
        <li>WAKAME GURKEN SALAT</li><li>PICKLES</li><li>GYOZA TEIGTASCHEN</li><li>SUSHI CAKE</li>
      </ul>
    </div>
    <div class="block set-2">
      <h2>SET 2 &nbsp;&nbsp;31,90€</h2>
      <ul>
        <li>HOSOMAKI</li><li>FUTOMAKI</li><li>PICKLES</li><li>SUSHI "THUNA" CAKE</li>
        <li>Crispy AUBERGINEN mit Mayo</li><li>AUBERGINE DENGAKU</li>
      </ul>
    </div>
    <div class="block set-3">
      <h2>SET 3 &nbsp;&nbsp;28,90€</h2>
      <ul>
        <li>HOSOMAKI</li><li>URAMAKI</li><li>NIGIRI</li><li>GEMÜSE TEMPURA</li>
        <li>Crispy TOFUSTICKS mit Mayo</li><li>WAKAME SHIRA AE</li>
      </ul>
    </div>
  </section>

  <section class="page page-dishes" aria-label="Speisen à la carte">
    <div class="food-photo salmon" style="left:-20px;top:-25px;width:130px;height:100px" role="img" aria-label="Foto: Sushi-Rolle mit Lachs"></div>
    <div class="food-photo roll" style="left:330px;top:-10px;width:80px;height:100px" role="img" aria-label="Foto: Sushi-Rolle mit Sesam"></div>
    <div class="food-photo sprout" style="left:-20px;top:120px;width:90px;height:90px" role="img" aria-label="Foto: Kressesprossen"></div>
    <div class="food-photo salmon" style="left:-25px;top:175px;width:75px;height:130px" role="img" aria-label="Foto: Sushi mit Lachs und Kaviar"></div>
    <div class="food-photo fish" style="left:-20px;top:300px;width:90px;height:80px" role="img" aria-label="Foto: Nigiri-Scheibe"></div>
    <div class="food-photo salmon" style="left:352px;top:230px;width:60px;height:140px" role="img" aria-label="Foto: Sushi-Rolle mit Lachs"></div>
    <div class="food-photo roll" style="left:-30px;top:445px;width:100px;height:120px" role="img" aria-label="Foto: Sushi-Rolle mit Stäbchen"></div>
    <div class="food-photo salmon" style="left:270px;top:465px;width:140px;height:100px" role="img" aria-label="Foto: Sushi mit Lachs und Sprossen"></div>

    <h1 class="brand">MOREVI</h1>

    <div class="block starters">
      <h2>VORSPEISEN</h2>
      <ul>
        <li>MISO SUPPE <span class="price">5,50€</span></li>
        <li>EDAMAME MIT SALZ/CHILI <span class="price">4,50€</span></li>
        <li>SEIDENTOFU in hausgemachter Sauce mit Mandeln <span class="price">5,50€</span></li>
      </ul>
    </div>

    <div class="block sushi">
      <h2>SUSHI</h2>
      <ul style="line-height:13.6px">
        <li style="line-height:13.6px">URAMAKI mit Tempuragemüse <span class="price">8,90€</span></li>
        <li style="line-height:13.6px">FUTOMAKI wechselndes Gemüse <span class="price">8,00€</span></li>
        <li style="line-height:13.6px">URAMAKI mit Austernpilze <span class="price">7,50€</span></li>
        <li style="line-height:13.6px">HOSOMAKI Gurke Avocado <span class="price">5,50€</span></li>
        <li style="line-height:13.6px">HOSOMAKI Gurke Shiitake <span class="price">5,50€</span></li>
        <li style="line-height:13.6px">TOMATEN NIGIRI <span class="price">4,50€</span></li>
      </ul>
    </div>

    <div class="block small">
      <h2>KLEINE GERICHTE</h2>
      <ul>
        <li style="line-height:13.6px">GEMÜSE TEMPURA <span class="price">8,00€</span></li>
        <li style="line-height:13.6px">Crispy TOFUSTICKS mit Mayo <span class="price">8,00€</span></li>
        <li style="line-height:13.6px">KÜRBISKROKETTEN mit TANGASHU <span class="price">7,90€</span></li>
        <li style="line-height:13.6px">SUSHI "THUNA" CAKE <span class="price">6,90€</span></li>
        <li style="line-height:13.6px">SUSHI CAKE CLASSIC <span class="price">6,00€</span></li>
        <li style="line-height:13.6px">AUBERGINE DENGAKU <span class="price">5,50€</span></li>
      </ul>
    </div>

    <div class="block mains">
      <h2>HAUPTSPEISEN</h2>
      <ul>
        <li class="wrap">Herrlich cremiges KATSU CURRY mit knusprigen Auberginensticks, Reis &amp; Pickles<br><span class="price">17,90€</span></li>
        <li class="wrap">RAMEN SUPPE mit Nudeln, Gemüse &amp; Tofu<br><span class="price">14,90€</span></li>
        <li style="line-height:11.5px">CHIRASHI SUSHI BOWL <span class="price">13,90€</span></li>
        <li class="wrap">SOMMERSALATE mit Sesamdressing &amp; crispy Tofusticks mit Mayo <span class="price">12,50€</span></li>
      </ul>
    </div>

    <div class="block desserts">
      <h2>DESSERT</h2>
      <ul>
        <li style="line-height:13.6px">CHEESECAKE mit Beeren <span class="price">6,50€</span></li>
        <li style="line-height:13.6px">PANA COTTA mit Beeren <span class="price">5,90€</span></li>
        <li style="line-height:13.6px">SORBET des Tages <span class="price">5,50€</span></li>
        <li style="line-height:13.6px">SORBET des Tages mit Schuss <span class="price">6,90€</span></li>
      </ul>
    </div>

    <p class="vegan-tag">All Vegan</p>
    <p class="allergy-note">Bitte teilen Sie dem Service unbedingt Allergien mit und fragen Sie nach<br>der Allergiker-Menükarte</p>
  </section>

</main>
</body>
</html>
```